Summer Drinks Flyer for Coffee Shop

We are a coffee shop in London and would like to have a cool and nice flyer for our summer drinks (juices and frozen drink) flyer - see on the attached file for the list

Attached you can find an "attempt" - please note that I would no necessary need the image below.

I also attache our new logo.

thank you

Industry/Entity Type

Coffee Shop

```html
<!DOCTYPE html>
<html lang="en">
<head>
<meta charset="utf-8">
<title>Limonella – New Summer Drinks Menu</title>
<link rel="stylesheet" href="https://fonts.googleapis.com/css2?family=Courgette&family=Ubuntu:wght@400;500&family=Arvo:wght@700&display=swap">
<style>
  :root {
    --backdrop: #e6e6e6;
    --paper: #ffffff;
    --gold: #c9a14a;
    --green: #8cc63f;
    --pink: #e8356f;
    --teal: #7fcfcf;
    --purple: #a45aad;
    --ink: #2d2d2d;
    --script: "Courgette", cursive;
    --body: "Ubuntu", sans-serif;
    --price: "Arvo", serif;
  }
  * { box-sizing: border-box; margin: 0; padding: 0; }
  html, body { width: 1200px; height: 810px; overflow: hidden; }
  body { background: var(--backdrop); font-family: var(--body); color: var(--ink); }

  .flyer {
    position: absolute; left: 320px; top: 15px;
    width: 560px; height: 780px;
    background: var(--paper);
    overflow: hidden;
    box-shadow: 0 4px 18px rgba(0,0,0,.18);
  }

  .brand {
    position: absolute; top: 22px; left: 300px;
    display: flex; align-items: center; gap: 8px;
    font-family: var(--body); font-size: 32px; color: var(--gold);
    letter-spacing: 1px;
  }
  .brand-dot { width: 14px; height: 14px; border-radius: 50%; background: var(--gold); }

  .fruit-photo {
    position: absolute; left: 0; top: 70px; width: 560px; height: 150px;
    background: linear-gradient(90deg, #e2455c 0%, #f5a623 30%, #cfe8ee 50%, #f7b733 70%, #8cc63f 90%, #dfeef2 100%);
    opacity: .75;
  }

  .title-band {
    position: absolute; left: 30px; top: 180px; width: 530px; height: 56px;
    background: var(--green);
    display: flex; align-items: center; justify-content: center;
    font-family: var(--script); font-size: 29px; color: #fff; letter-spacing: 1px;
  }

  .ribbon {
    position: absolute; left: 0; height: 36px;
    clip-path: polygon(0 0, calc(100% - 18px) 0, 100% 50%, calc(100% - 18px) 100%, 0 100%);
    font-family: var(--script); font-size: 20px; color: #fff;
    display: flex; align-items: center; padding-left: 70px;
  }
  .ribbon--pink { top: 250px; width: 440px; background: var(--pink); }
  .ribbon--teal { top: 350px; width: 400px; background: var(--teal); }
  .ribbon--purple { top: 530px; width: 380px; background: var(--purple); }

  .drink-list {
    position: absolute; left: 90px; list-style: none;
    font-size: 15px; line-height: 21px;
  }
  .drink-list--frozen { top: 294px; }
  .drink-list--juices { top: 394px; }
  .drink-list--coffees { top: 574px; }

  .offer {
    position: absolute; width: 112px; height: 112px; border-radius: 50%;
    border: 4px solid #fff; outline: 2px solid currentColor;
    display: flex; align-items: center; justify-content: center; text-align: center;
    font-family: var(--script); font-size: 15px; line-height: 19px; color: #fff;
  }
  .offer span { color: #fff; }
  .offer--mint { left: 370px; top: 380px; background: var(--teal); color: var(--teal); }
  .offer--syrup { left: 340px; top: 565px; background: var(--purple); color: var(--purple); }
  .offer .big { font-size: 19px; }

  .price {
    position: absolute; font-family: var(--price); font-size: 30px;
  }
  .price--pink { left: 430px; top: 300px; color: var(--pink); }
  .price--teal { left: 440px; top: 490px; color: var(--teal); }
  .price--purple { left: 420px; top: 680px; color: var(--purple); }

  .tag {
    position: absolute; right: 0; width: 60px; height: 28px;
    clip-path: polygon(14px 0, 100% 0, 100% 100%, 14px 100%, 0 50%);
  }
  .tag--pink { top: 342px; background: var(--pink); }
  .tag--teal { top: 532px; background: var(--teal); }
  .tag--purple { top: 722px; background: var(--purple); }

  .splash-photo {
    position: absolute; left: 270px; top: 470px; width: 290px; height: 240px;
    background: radial-gradient(ellipse at 60% 50%, rgba(120,170,200,.35), rgba(255,255,255,0) 70%);
  }
</style>
</head>
<body>
  <main class="flyer">
    <div class="fruit-photo" role="img" aria-label="Fresh fruit pieces and ice cubes splashing across the top"></div>
    <div class="splash-photo" role="img" aria-label="Water splash with lime slice and mint leaves"></div>

    <div class="brand"><span class="brand-dot"></span>Limonella</div>

    <h1 class="title-band">NEW SUMMER DRINKS MENU</h1>

    <h2 class="ribbon ribbon--pink">Frozen Fruit Drinks</h2>
    <ul class="drink-list drink-list--frozen">
      <li>Strawberry and banana</li>
      <li>Pineapple, mango and banana</li>
    </ul>
    <div class="price price--pink">£2.95</div>
    <div class="tag tag--pink"></div>

    <h2 class="ribbon ribbon--teal">Fruit Juices</h2>
    <ul class="drink-list drink-list--juices">
      <li>Orange and carrot</li>
      <li>Orange and pineapple</li>
      <li>Pineapple and apple</li>
      <li>Apple and kiwi</li>
      <li>Carrot and ginger</li>
    </ul>
    <div class="offer offer--mint"><span>add Mint or<br>Ginger for<br><b class="big">Free</b></span></div>
    <div class="price price--teal">£2.95</div>
    <div class="tag tag--teal"></div>

    <h2 class="ribbon ribbon--purple">Iced-Coffees</h2>
    <ul class="drink-list drink-list--coffees">
      <li>Iced Coffee</li>
      <li>Iced Latte</li>
      <li>Iced Chocolate Drink</li>
    </ul>
    <div class="offer offer--syrup"><span>add Syrup<br>shot for<br><b class="big">10 p</b></span></div>
    <div class="price price--purple">£2.95</div>
    <div class="tag tag--purple"></div>
  </main>
</body>
</html>
```